Need a design package for hair towels wrap

We need package design for hair towel wrap ( 3 pack) brand name is The Quorin. We are looking for simple, contemporary and unique design, color palette 2-3 colors. Paper Box size is 9*8*3 inches with PVC window.Actual picture of the product won't be on the package.Attached Brand Logo and description for the package. Barcode needed to be included on the design package.It will be provided later. Attached sample of the box from manufacturer, and instruction for towel wrap which idea I like, if you could make something similar to it, would be great.

Target Market(s)

Zelvora

Industry/Entity Type

Hair

Colors
848484
f5f5f5
faa54b
333333

Requirements
Must have
• Clean, contemporary design.

```html
<!DOCTYPE html>
<html lang="en">
<head>
<meta charset="utf-8">
<title>The Quorin – Microfiber Hair Towel Wrap Box</title>
<link href="https://fonts.googleapis.com/css2?family=Montserrat:wght@700;800&family=Arimo:ital,wght@0,400;0,700;1,400&display=swap" rel="stylesheet">
<style>
  :root{
    --page:#f5f5f5;
    --pink:#ee7fab;
    --pink-top:#f08bb3;
    --pink-side:#df77a2;
    --pink-deep:#cf4a86;
    --pink-edge:#c43f7c;
    --blossom:#f9c6dc;
    --gold:#faa54b;
    --gold-dark:#c98a2e;
    --ink:#333333;
    --title:#2f2a3a;
    --white:#ffffff;
  }
  *{margin:0;padding:0;box-sizing:border-box}
  html,body{width:1200px;height:960px;overflow:hidden;background:var(--page)}
  .canvas{position:relative;width:1200px;height:960px}

  /* Lid panel */
  .top-panel{
    position:absolute;left:330px;top:60px;width:810px;height:140px;
    background:var(--pink-top);overflow:hidden;
  }
  .top-panel svg{position:absolute;inset:0}
  .top-brand{
    position:absolute;left:50%;top:50%;transform:translate(-50%,-50%);
    display:flex;align-items:center;gap:10px;
    font-family:"Montserrat",sans-serif;font-weight:800;font-size:24px;color:var(--ink);letter-spacing:.5px;
    white-space:nowrap;
  }
  .top-brand .brand-mark{width:18px;height:18px}

  /* Side panel */
  .side-panel{
    position:absolute;left:60px;top:200px;width:270px;height:700px;
    background:linear-gradient(180deg,#e27aa4,#d86c98);
    overflow:hidden;
  }
  .side-copy{
    position:absolute;left:50%;top:50%;width:620px;
    transform:translate(-50%,-50%) rotate(90deg);
    color:var(--white);font-family:"Arimo",sans-serif;font-size:13px;line-height:1.55;
    display:flex;gap:24px;align-items:flex-start;
  }
  .side-copy .features{flex:1}
  .side-copy ul{list-style:none}
  .side-copy li::before{content:"• "}
  .side-copy .label{font-weight:700;margin-top:6px}
  .tip-box{
    width:150px;flex:none;border:1.5px solid rgba(255,255,255,.8);border-radius:12px;
    padding:10px 12px;font-style:italic;font-size:12.5px;
  }
  .tip-box strong{font-style:normal;display:block}

  /* Front panel */
  .front-panel{position:absolute;left:330px;top:200px;width:810px;height:700px;overflow:hidden}
  .front-panel svg{position:absolute;inset:0}

  .brand{
    position:absolute;left:110px;top:90px;display:flex;align-items:center;gap:12px;
    font-family:"Montserrat",sans-serif;font-weight:800;font-size:34px;color:var(--ink);letter-spacing:.5px;
  }
  .brand-mark{width:26px;height:26px;background:var(--gold);flex:none}

  .product-title{
    position:absolute;left:0;right:0;top:548px;text-align:center;
    font-family:"Arimo",sans-serif;font-weight:700;font-size:40px;color:var(--title);
  }
  .tagline{
    position:absolute;left:0;right:0;top:612px;text-align:center;
    font-family:"Arimo",sans-serif;font-size:20px;color:var(--white);
  }
</style>
</head>
<body>
<main class="canvas">

  <section class="top-panel">
    <svg width="810" height="140" viewBox="0 0 810 140">
      <defs>
        <linearGradient id="lidArtLeft" x1="0" x2="1">
          <stop offset="0" stop-color="var(--white)" stop-opacity=".75"/>
          <stop offset="1" stop-color="var(--blossom)" stop-opacity="0"/>
        </linearGradient>
        <linearGradient id="lidArtRight" x1="1" x2="0">
          <stop offset="0" stop-color="var(--white)" stop-opacity=".75"/>
          <stop offset="1" stop-color="var(--blossom)" stop-opacity="0"/>
        </linearGradient>
      </defs>
      <rect class="lid-art" role="img" aria-label="White swirls with pink blossoms" x="10" y="15" width="250" height="110" rx="40" fill="url(#lidArtLeft)"/>
      <rect class="lid-art" role="img" aria-label="White swirls with pink blossoms" x="550" y="15" width="250" height="110" rx="40" fill="url(#lidArtRight)"/>
    </svg>
    <div class="top-brand"><span class="brand-mark"></span>THE QUORIN</div>
  </section>

  <section class="side-panel">
    <div class="side-copy">
      <div class="features">
        <ul>
          <li>Fits all head sizes.</li>
          <li>Suitable for all hair types and lengths.</li>
          <li>Holds extra long hair.</li>
          <li>Absorb approximately 70% of the water within 10 min.</li>
          <li>Less time blow drying means healthier hair.</li>
          <li>Reduce risk of split ends, breakage and frizz.</li>
        </ul>
        <p class="label">Material:</p>
        <p>The Quorin hair towel is made from innovative, luxury quality, light microfiber material to create ultra absorption and comfort. It dries your hair up to 4 times faster than a regular towel. It is soft, light and gentle for your hair and skin. It will leave your hair healthy and silky.</p>
      </div>
      <div class="tip-box"><strong>Natural Hair tips:</strong>Never rub your hair when you using towel.</div>
    </div>
  </section>

  <section class="front-panel">
    <svg width="810" height="700" viewBox="0 0 810 700">
      <defs>
        <linearGradient id="goldLine" x1="0" x2="1">
          <stop offset="0" stop-color="var(--gold-dark)"/>
          <stop offset=".5" stop-color="var(--gold)"/>
          <stop offset="1" stop-color="var(--gold-dark)"/>
        </linearGradient>
        <linearGradient id="floral" x1="0" y1="0" x2="1" y2="1">
          <stop offset="0" stop-color="var(--blossom)" stop-opacity=".9"/>
          <stop offset=".55" stop-color="var(--white)" stop-opacity=".7"/>
          <stop offset="1" stop-color="var(--blossom)" stop-opacity=".9"/>
        </linearGradient>
        <radialGradient id="towel" cx=".5" cy=".45" r=".6">
          <stop offset="0" stop-color="#ffffff"/>
          <stop offset="1" stop-color="#dcdcdc"/>
        </radialGradient>
      </defs>

      <rect class="panel-bg" width="810" height="700" fill="var(--pink)"/>

      <path class="floral-art" role="img" aria-label="White swirling vine with pink blossoms"
            d="M560,20 L800,20 L800,300 C760,330 720,370 690,420 C640,420 600,390 600,350 L600,240 C560,220 540,180 540,140 Z"
            fill="url(#floral)"/>

      <path class="lower-band" d="M0,500 C260,480 540,400 810,300 L810,700 L0,700 Z" fill="var(--pink-deep)"/>
      <path class="gold-swoosh" d="M0,492 C260,472 560,392 810,292" fill="none" stroke="url(#goldLine)" stroke-width="7"/>

      <g class="window" role="img" aria-label="Clear window showing rolled white microfiber towels">
        <g fill="var(--pink-edge)">
          <circle cx="235" cy="270" r="86"/><circle cx="355" cy="262" r="86"/>
          <circle cx="228" cy="385" r="86"/><circle cx="348" cy="392" r="86"/>
          <circle cx="290" cy="328" r="94"/>
        </g>
        <g fill="url(#towel)">
          <circle cx="235" cy="270" r="77"/><circle cx="355" cy="262" r="77"/>
          <circle cx="228" cy="385" r="77"/><circle cx="348" cy="392" r="77"/>
          <circle cx="290" cy="328" r="85"/>
        </g>
      </g>
    </svg>

    <div class="brand"><span class="brand-mark"></span>THE QUORIN</div>
    <h1 class="product-title">Microfiber Hair Towel Wrap</h1>
    <p class="tagline">The softest, ultra-absorbent, light &amp; safest Towel for your beautiful hair.</p>
  </section>

</main>
</body>
</html>
```